Funeral Services Web Site

We need a website for a Funeral Services company. The choice of colors is free of charge. One Page Website with 8 sections. Menu: - Home - Our Services - Obituaries -> link to another page. - Our Shop - Funeral Monument - Funeral Contract - Contact Us

Target Market(s)

Every one need Funeral Services

Coding

Coded - Design and coding required

Number of Pages Required

2 page

Font styles to use
Sans Serif
Script

Colors

Designer to choose colors to be used in the design.

```html
<!DOCTYPE html>
<html lang="en">
<head>
<meta charset="utf-8">
<title>Maison Verlaine – Funeral Services</title>
<link href="https://fonts.googleapis.com/css2?family=Lato:wght@300;400;700&display=swap" rel="stylesheet">
<style>
:root{
  --brown:#8b7156;
  --brown-dark:#6e5741;
  --taupe:#a89078;
  --ink:#2f2a26;
  --muted:#6b645d;
  --paper:#ffffff;
  --mist:#f1efec;
  --line:#c9c2b9;
  --foot:#e9e7e4;
}
*{margin:0;padding:0;box-sizing:border-box}
html,body{width:1200px;height:3160px;overflow:hidden;background:var(--paper)}
body{font-family:'Lato',sans-serif;color:var(--ink);position:relative}
.abs{position:absolute}
.btn{display:inline-block;border:2px solid currentColor;border-radius:30px;padding:12px 30px;font-size:15px;font-weight:700;letter-spacing:1px;text-transform:uppercase}
/* header */
.site-header{left:0;top:0;width:1200px;height:112px;background:var(--paper);z-index:3}
.brand{left:160px;top:22px;display:flex;align-items:center;gap:14px}
.brand-mark{width:60px;height:60px;border-radius:50%;background:var(--brown)}
.brand-name{font-size:30px;font-weight:700;color:var(--ink);line-height:1.05;width:200px}
.top-links{right:100px;top:24px;display:flex;gap:30px;font-size:17px;color:var(--ink)}
.main-nav{right:100px;top:70px;display:flex;gap:40px;font-size:19px;font-weight:700;color:var(--ink)}
/* hero */
.hero{left:0;top:112px;width:1200px;height:640px;background:linear-gradient(100deg,#5e564f 0%,#8a8178 40%,#c9c0b4 70%,#a4926e 100%)}
.hero-copy{left:140px;top:250px;color:#fff;width:520px}
.hero-copy h1{font-size:40px;font-weight:700;margin-bottom:12px;white-space:nowrap}
.hero-copy p{font-size:16px;line-height:1.45;margin-bottom:34px;opacity:.92;width:420px}
.dots{display:flex;gap:10px}
.dots span{width:12px;height:12px;border-radius:50%;border:2px solid currentColor}
.dots span.on{background:currentColor}
/* about */
.emblem{left:240px;top:780px;width:300px;height:310px;border-radius:50%;background:radial-gradient(circle,#ddd6cd 0%,#f6f3ef 70%,#fff 100%)}
.about{left:592px;top:790px;width:470px}
.about h2{font-size:38px;font-weight:700;margin-bottom:20px}
.about p{font-size:15px;line-height:1.55;color:var(--muted);margin-bottom:30px}
.about .btn{color:var(--ink)}
/* services */
.services-band{left:0;top:1140px;width:1200px;height:580px}
.services-title{left:0;top:1238px;width:1200px;text-align:center;color:#fff;font-size:34px;font-weight:700}
.service{top:1350px;width:300px;height:240px;border:2px solid rgba(255,255,255,.7);color:#fff;text-align:center;padding:60px 24px 0}
.service-icon{position:absolute;left:50%;top:-40px;transform:translateX(-50%);width:80px;height:80px;border-radius:50%;background:#fff;display:flex;align-items:center;justify-content:center}
.service h3{font-size:19px;font-weight:700;line-height:1.3;margin-bottom:14px}
.service p{font-size:13px;line-height:1.45;opacity:.85}
/* cards */
.card{top:1830px;width:440px;height:300px;border-radius:26px;overflow:hidden;color:#fff;text-align:center;padding-top:80px}
.card h3{font-size:30px;font-weight:400;margin-bottom:10px}
.card p{font-size:15px;line-height:1.45;width:300px;margin:0 auto 22px}
/* shop */
.shop{left:0;top:2240px;width:1200px;height:600px;background:linear-gradient(180deg,#8f8478 0%,#6f6459 45%,#9a8260 100%)}
.shop-copy{left:260px;top:2355px;width:680px;text-align:center;color:#fff}
.shop-copy h2{font-size:40px;font-weight:400;margin-bottom:18px}
.shop-copy p{font-size:16px;line-height:1.5;margin-bottom:40px}
/* footer */
.site-footer{left:0;top:2790px;width:1200px;height:300px;background:var(--foot)}
.foot-emblem{left:150px;top:2810px;width:200px;height:220px;border-radius:50%;background:radial-gradient(circle,#d2c9be 0%,var(--foot) 72%)}
.foot-col{top:2830px}
.foot-col h4{font-size:24px;font-weight:700;margin-bottom:22px}
.foot-col li{list-style:none;font-size:15px;line-height:1.35;color:var(--muted);margin-bottom:12px;display:flex;align-items:center;gap:12px;white-space:nowrap}
.foot-contact{left:410px;width:240px}
.foot-links{left:672px;width:200px}
.foot-follow{left:900px;width:200px}
.dot-icon{width:24px;height:24px;border-radius:50%;background:var(--brown);flex:none}
.copyright{left:0;top:3090px;width:1200px;height:70px;background:#dcd9d5;text-align:center;line-height:70px;font-size:14px;color:var(--muted)}
</style>
</head>
<body>

<header class="site-header abs">
  <div class="brand abs"><span class="brand-mark"></span><span class="brand-name">Maison Verlaine</span></div>
  <nav class="top-links abs"><span>Funeral Contract</span><span>Contact Us</span></nav>
  <nav class="main-nav abs"><span>Our Services</span><span>Obituaries</span><span>Our Shop</span><span>Funeral Monument</span></nav>
</header>

<section class="hero abs" role="img" aria-label="Photo of a funeral chapel with flowers beside a casket"></section>
<div class="hero-copy abs">
  <h1>Welcome to Maison Verlaine</h1>
  <p>Pellentesque faucibus ut accumsan ultrices elit Maecenas at justo et velit placerat.</p>
  <span class="btn">Read more</span>
</div>
<div class="dots abs" style="left:574px;top:620px;color:#fff"><span class="on"></span><span></span><span></span></div>
<svg class="abs" style="left:0;top:640px" width="1200" height="120" viewBox="0 0 1200 120" aria-hidden="true">
  <path d="M0 40 Q600 150 1200 40 L1200 120 L0 120Z" fill="#fff"/>
  <path d="M0 40 Q600 150 1200 40" fill="none" stroke="var(--taupe)" stroke-width="4"/>
</svg>

<div class="emblem abs" role="img" aria-label="Emblem of a dove with spread wings"></div>
<section class="about abs">
  <h2>About Maison Verlaine</h2>
  <p>Pellentesque faucibus ut accumsan ultrices elit Maecenas at justo et velit placerat molestie donec dictum lectus non odio. Cras a ante vitae enim iaculis aliquam. Mauris nunc quam venenatis nec euismod sit amet egestas placerat est. Pellentesque habitant morbi tristique senectus et netus et malesuada fames ac turpis egestas.</p>
  <span class="btn">Read more</span>
</section>

<svg class="services-band abs" viewBox="0 0 1200 580" aria-hidden="true">
  <path d="M0 70 Q300 0 650 40 T1200 30 L1200 500 Q800 580 500 540 T0 520Z" fill="var(--brown)"/>
  <path d="M760 530 Q1000 520 1200 470 L1200 500 Q1000 555 760 530Z" fill="#8d8a86"/>
</svg>
<h2 class="services-title abs">Our Services</h2>
<div class="service abs" style="left:128px">
  <span class="service-icon"><svg width="40" height="40" viewBox="0 0 40 40"><path d="M6 22 L15 14 L22 18 L34 10 M10 26 L18 32 L30 22" fill="none" stroke="var(--brown)" stroke-width="3" stroke-linecap="round"/></svg></span>
  <h3>Personalized and dignified support from the first moments</h3>
  <p>Funeral advisors guide your family with care, from the very first call.</p>
</div>
<div class="service abs" style="left:450px">
  <span class="service-icon"><svg width="40" height="40" viewBox="0 0 40 40"><rect x="10" y="6" width="20" height="28" rx="2" fill="none" stroke="var(--brown)" stroke-width="3"/><path d="M15 14h10M15 20h10M15 26h6" stroke="var(--brown)" stroke-width="3"/></svg></span>
  <h3>Assistance in all administrative procedures</h3>
  <p>We take the weight of every form and step, so you can focus on family.</p>
</div>
<div class="service abs" style="left:772px">
  <span class="service-icon"><svg width="40" height="40" viewBox="0 0 40 40"><circle cx="20" cy="20" r="13" fill="none" stroke="var(--brown)" stroke-width="3"/><path d="M14 20l4 4 8-8" fill="none" stroke="var(--brown)" stroke-width="3"/></svg></span>
  <h3>Offer him his song to pay him a last tribute</h3>
  <p>Choose a personal piece of music to honour a life in a fitting way.</p>
</div>
<div class="dots abs" style="left:574px;top:1645px;color:#8d8a86"><span class="on"></span><span></span><span></span></div>

<article class="card abs" style="left:152px;background:linear-gradient(160deg,#9a7a50,#7a5b3a)" role="img" aria-label="Photo of a marble funeral monument">
  <h3>Funeral Monument</h3>
  <p>Lorem ipsum dolor sit amet consectetur adipiscing elit sed do eiusmod.</p>
  <span class="btn">Read more</span>
</article>
<article class="card abs" style="left:608px;background:linear-gradient(160deg,#8f9081,#6b6a5e)" role="img" aria-label="Photo of hands writing a letter">
  <h3>Submit your last wishes</h3>
  <p>Lorem ipsum dolor sit amet consectetur adipiscing elit sed do eiusmod.</p>
  <span class="btn">Click here</span>
</article>

<section class="shop abs" role="img" aria-label="Photo of a showroom with wooden caskets and flower arrangements"></section>
<svg class="abs" style="left:0;top:2236px" width="1200" height="90" viewBox="0 0 1200 90" aria-hidden="true">
  <path d="M0 0 H1200 V20 Q700 100 0 40Z" fill="#fff"/>
  <path d="M0 40 Q700 100 1200 20" fill="none" stroke="var(--taupe)" stroke-width="4"/>
</svg>
<div class="shop-copy abs">
  <h2>Our Shop</h2>
  <p>Pellentesque faucibus ut accumsan ultrices elit Maecenas at justo et velit placerat molestie donec dictum lectus non odio. Cras a ante vitae enim iaculis aliquam. Mauris nunc quam venenatis nec euismod sit amet egestas placerat est.</p>
  <span class="btn">Click here</span>
</div>
<svg class="abs" style="left:0;top:2740px" width="1200" height="60" viewBox="0 0 1200 60" aria-hidden="true">
  <path d="M0 60 Q500 0 1200 40 V60Z" fill="var(--foot)"/>
</svg>

<footer class="site-footer abs"></footer>
<div class="foot-emblem abs" role="img" aria-label="Emblem of a dove with spread wings"></div>
<div class="foot-col foot-contact abs">
  <h4>Contact Us</h4>
  <ul>
    <li><svg width="20" height="20" viewBox="0 0 20 20"><path d="M10 2a6 6 0 0 0-6 6c0 5 6 10 6 10s6-5 6-10a6 6 0 0 0-6-6z" fill="var(--muted)"/></svg><span>12 Rue des Tilleuls<br>4410 Valmont</span></li>
    <li><svg width="20" height="20" viewBox="0 0 20 20"><path d="M4 2h4l2 5-3 2a10 10 0 0 0 4 4l2-3 5 2v4a2 2 0 0 1-2 2A16 16 0 0 1 2 4a2 2 0 0 1 2-2z" fill="var(--muted)"/></svg>(555) 0142 7731</li>
    <li><svg width="20" height="20" viewBox="0 0 20 20"><rect x="2" y="4" width="16" height="12" fill="none" stroke="var(--muted)" stroke-width="2"/><path d="M2 4l8 7 8-7" fill="none" stroke="var(--muted)" stroke-width="2"/></svg>info@verlaine.example</li>
  </ul>
</div>
<div class="foot-col foot-links abs">
  <h4>Quick links</h4>
  <ul><li>Our Services</li><li>Obituaries</li><li>Our Shop</li><li>Funeral Monument</li><li>Funeral Contract</li><li>Contact Us</li></ul>
</div>
<div class="foot-col foot-follow abs">
  <h4>Follow Us</h4>
  <ul><li><span class="dot-icon"></span>Updates</li><li><span class="dot-icon"></span>Community</li><li><span class="dot-icon"></span>Network</li><li><span class="dot-icon"></span>Gallery</li></ul>
</div>
<div class="copyright abs">Copyright © 2019 All rights reserved</div>

</body>
</html>
```